Orthopedic Arm Surgeon Brochure

Bifold modern design. I will supply the text, my photo, and photos of my textbooks. Prefer colors in the greens, blues, greys. For more information visit LimbForwardClinic.com Please feel free to e-mail me with any questions. Current brochure attached; I want to modernize this, get rid of frames, and change the text.

Target Market(s)

High-end market

Colors
3176b5
33a6d7
33b8a4
abd036
876aae
b768aa

Requirements
Must have
• Beautiful finishes
Should not have
• Bright reds, yellows, oranges that emit fear

```html
<!DOCTYPE html>
<html lang="en">
<head>
<meta charset="utf-8">
<title>Orthopedic Arm Surgeon Brochure</title>
<link href="https://fonts.googleapis.com/css2?family=Lato:ital,wght@0,400;0,700;0,900;1,400;1,700;1,900&display=swap" rel="stylesheet">
<style>
  :root{
    --bg:#e8e3df;
    --paper:#ffffff;
    --blue:#33a6d7;
    --blue-deep:#3176b5;
    --teal:#33b8a4;
    --green:#1c7a4c;
    --ink:#3c3c3c;
    --muted:#7a7a7a;
    --line:#d6d6d6;
  }
  *{box-sizing:border-box;margin:0;padding:0}
  html,body{width:1200px;height:1200px;overflow:hidden;background:var(--bg)}
  body{font-family:'Lato',sans-serif;color:var(--ink);position:relative}
  .spread{position:absolute;left:160px;width:880px;height:560px;background:var(--paper);box-shadow:0 6px 18px rgba(0,0,0,.18);overflow:hidden}
  .spread--outside{top:22px}
  .spread--inside{top:612px}
  .spine{position:absolute;left:437px;top:0;width:6px;height:100%;background:linear-gradient(90deg,rgba(0,0,0,0),rgba(0,0,0,.08),rgba(0,0,0,0))}
  .panel{position:absolute;top:0;width:440px;height:560px}
  .panel--left{left:0}
  .panel--right{left:440px}
  .band{position:absolute;left:0;width:440px}
  .ph{position:absolute}
  .bio{position:absolute;left:34px;top:190px;width:375px;font-size:9.6px;line-height:1.42}
  .bio p{margin-bottom:3px}
  .loc-title{color:var(--green);font-weight:900;font-size:11px;margin:8px 0 10px}
  .locations{display:grid;grid-template-columns:1fr 1fr;gap:14px 22px}
  .loc h4{font-size:10.5px;font-weight:900;margin-bottom:3px}
  .loc p{font-size:9.4px;line-height:1.3;padding-left:14px;position:relative}
  .loc svg{position:absolute;left:0;top:2px}
  .brand{position:absolute;left:0;width:440px;top:190px;text-align:center;color:var(--green);font-weight:900;font-size:19px;letter-spacing:.5px}
  .brand small{display:block;font-size:10px;font-weight:400;letter-spacing:.3px}
  .brand .mark{display:inline-block;width:10px;height:10px;border-radius:50%;background:var(--green);margin-right:7px;vertical-align:2px}
  .tags{position:absolute;left:30px;top:250px;width:380px;display:flex;flex-wrap:wrap;justify-content:center;gap:9px 10px}
  .tag{border:1px solid var(--line);box-shadow:0 1px 3px rgba(0,0,0,.12);padding:5px 14px;font-size:11px;font-weight:700;color:#444;background:#fff}
  .phone{position:absolute;left:0;width:440px;top:372px;text-align:center;color:var(--green);font-weight:900;font-size:22px}
  .phone svg{vertical-align:-2px;margin-right:6px}
  .appt{position:absolute;left:0;width:440px;top:402px;text-align:center;font-size:9px;color:var(--muted)}
  .url-band{position:absolute;left:0;width:440px;bottom:14px;text-align:center;color:#fff;font-size:10px;letter-spacing:2.5px}
  .copy{position:absolute;font-size:8.6px;line-height:1.34}
  .copy h2{color:var(--green);font-style:italic;font-weight:900;font-size:13px;margin:6px 0 4px}
  .copy p{margin-bottom:3px}
  .copy .link{font-weight:900;font-size:10px;color:#333;margin-bottom:6px}
</style>
</head>
<body>

<!-- Outside spread -->
<section class="spread spread--outside">
  <div class="panel panel--left">
    <svg class="band" style="top:0" width="440" height="175" viewBox="0 0 440 175">
      <path d="M0 0H440V60C330 95 220 110 0 95Z" fill="var(--blue)"/>
      <path d="M0 95C220 110 330 95 440 60V70C330 110 220 125 0 110Z" fill="#e9f5fb"/>
    </svg>
    <div class="ph" role="img" aria-label="Portrait of the surgeon" style="left:30px;top:38px;width:120px;height:120px;border-radius:50%;border:5px solid var(--blue);background:linear-gradient(160deg,#c9ccd2,#5f6670)"></div>
    <div class="ph" role="img" aria-label="Covers of the surgeon's textbooks" style="left:180px;top:30px;width:200px;height:95px;background:linear-gradient(100deg,#2a4f8f,#8b2b3a 55%,#5a3d6e)"></div>
    <div class="bio">
      <p>Dr. Halvorsen is a nationally-recognized Upper Extremity Surgeon who has edited 7 textbooks, published over 45 original research papers and written 23 textbook chapters.</p>
      <p>Dr. Halvorsen graduated Cum Laude from Easton University and with honors from Northfield Medical School. He completed his residency in Orthopaedic Surgery at Westbrook University. In order to obtain expertise covering the entire upper extremity, he completed two fellowships, one in Hand Surgery and the other in Sports Medicine. He is board certified in Orthopaedic Surgery and has a Certificate of Additional Qualification in Hand Surgery.</p>
      <div class="loc-title">Dr. Halvorsen sees patients at the following locations:</div>
      <div class="locations">
        <div class="loc"><h4>Central Medical District</h4><p><svg width="8" height="11" viewBox="0 0 8 11"><path d="M4 0a4 4 0 0 1 4 4c0 3-4 7-4 7S0 7 0 4a4 4 0 0 1 4-4z" fill="var(--blue)"/><circle cx="4" cy="4" r="1.5" fill="#fff"/></svg>4120 Alder Street Suite 1016<br>Suite 202 Lakemont, TX<br>70001</p></div>
        <div class="loc"><h4>Riverbend</h4><p><svg width="8" height="11" viewBox="0 0 8 11"><path d="M4 0a4 4 0 0 1 4 4c0 3-4 7-4 7S0 7 0 4a4 4 0 0 1 4-4z" fill="var(--blue)"/><circle cx="4" cy="4" r="1.5" fill="#fff"/></svg>2280 Harbor View Dr Suite<br>202 Riverbend, TX 70002</p></div>
        <div class="loc"><h4>Oak Hollow</h4><p><svg width="8" height="11" viewBox="0 0 8 11"><path d="M4 0a4 4 0 0 1 4 4c0 3-4 7-4 7S0 7 0 4a4 4 0 0 1 4-4z" fill="var(--blue)"/><circle cx="4" cy="4" r="1.5" fill="#fff"/></svg>318 Willow Grove Dr. Oak Hollow,<br>TX 70003</p></div>
        <div class="loc"><h4>Stonebridge</h4><p><svg width="8" height="11" viewBox="0 0 8 11"><path d="M4 0a4 4 0 0 1 4 4c0 3-4 7-4 7S0 7 0 4a4 4 0 0 1 4-4z" fill="var(--blue)"/><circle cx="4" cy="4" r="1.5" fill="#fff"/></svg>9150 County Road West<br>Stonebridge, TX 70004</p></div>
      </div>
    </div>
  </div>

  <div class="panel panel--right">
    <div class="ph" role="img" aria-label="Photo of a person holding a sore wrist at a laptop" style="left:0;top:0;width:440px;height:175px;background:linear-gradient(120deg,#6b7a5e,#d8b6a4 55%,#eae6e0)"></div>
    <svg class="band" style="top:140px" width="440" height="60" viewBox="0 0 440 60">
      <path d="M0 30C150 10 300 5 440 0V60H0Z" fill="#fff"/>
      <path d="M0 30C150 10 300 5 440 0V4C300 9 150 16 0 36Z" fill="var(--teal)"/>
    </svg>
    <div class="brand"><span class="mark"></span>MERIDIAN<small>Orthopedic Group, L.L.P.</small></div>
    <div class="tags">
      <span class="tag">Carpal tunnel</span><span class="tag">Cubital Tunnel</span><span class="tag">Shoulder Pain.</span>
      <span class="tag">Trigger Finger</span><span class="tag">Elbow</span>
      <span class="tag">DeQuervain's tendinitis</span>
    </div>
    <div class="phone"><svg width="16" height="16" viewBox="0 0 24 24"><path d="M6.6 10.8a15 15 0 0 0 6.6 6.6l2.2-2.2c.3-.3.7-.4 1-.2 1.1.4 2.3.6 3.6.6.6 0 1 .4 1 1V20c0 .6-.4 1-1 1A17 17 0 0 1 3 4c0-.6.4-1 1-1h3.5c.6 0 1 .4 1 1 0 1.3.2 2.5.6 3.6.1.3 0 .7-.2 1z" fill="var(--ink)"/></svg>555-014-ARMS</div>
    <div class="appt">Appoinment can be made online through BookCareNow.com</div>
    <svg class="band" style="bottom:0" width="440" height="110" viewBox="0 0 440 110">
      <path d="M0 55C160 70 320 45 440 0V110H0Z" fill="var(--blue)"/>
      <path d="M0 45C160 60 320 38 440 -6V4C320 48 160 68 0 55Z" fill="var(--teal)"/>
    </svg>
    <div class="url-band">www.LimbForwardClinic.com</div>
  </div>
  <div class="spine"></div>
</section>

<!-- Inside spread -->
<section class="spread spread--inside">
  <div class="panel panel--left">
    <svg class="band" style="top:0" width="440" height="90" viewBox="0 0 440 90">
      <path d="M0 0H440V80C340 40 200 15 0 12Z" fill="var(--blue)"/>
      <path d="M0 12C200 15 340 40 440 80V88C340 50 200 24 0 22Z" fill="#e9f5fb"/>
    </svg>
    <div class="copy" style="left:30px;top:22px;width:385px">
      <h2>Carpal Tunnel<br>Syndrome</h2>
      <p>Carpal Tunnel Syndrome occurs when the main/median nerve to the hand gets pinched at the wrist. This leads to fingers feeling "numb", "asleep", "cold", like they "lack circulation" or have "pins and needles" in them. Carpal tunnel syndrome is usually worst at night or upon awakening. If you wake up at night with your hand numb or painfully asleep, and have to "shake it out" to get relief, you've probably got carpal tunnel syndrome. Symptoms also often occur with gripping, such as when driving, writing or holding books, cell phones or tools.</p>
      <p>Unless the carpal tunnel syndrome has led to nerve damage, initial treatment often involves splinting the wrist at night when asleep. If that doesn't work, the carpal tunnel can be released. The least invasive technique is the single-incision Endoscopic Carpal Tunnel Release. This quick, minimally invasive, outpatient procedure uses a small incision at the wrist without an incision in the hand. Compared to other techniques, there is decreased pain and a quicker return to work and other activities. There are no bandages, and hand washing and showering can be performed immediately. To see a video of an Endoscopic Carpal Tunnel Release please go to:</p>
      <p class="link">www.LimbForwardClinic.com</p>
      <h2>Cubital Tunnel Syndrome</h2>
      <p>Cubital tunnel syndrome occurs when the funny bone (ulnar) nerve gets pinched at the elbow. This leads to tingling and numbness of the small finger when the elbow is bent, usually at night or when talking on the phone. Numbness may also occur when the elbows is placed on a hard surface.</p>
      <p>Unless nerve damage has occurred, treatment starts with avoiding pressure on the elbow, and not resting the elbow on desks, arm rests, or other hard objects. Avoid prolonged elbow flexion: use the other hand to hold phones or get a hands-free device.</p>
      <p>If this fails, the least invasive definitive treatment is an Endoscopic Cubital Tunnel Release. This minimally invasive, outpatient procedure allows an early return to activities with a low complication rate. No splint is used after surgery. To see a video of an Endoscopic Cubital Tunnel Release please go to:</p>
      <p class="link">www.LimbForwardClinic.com</p>
    </div>
  </div>

  <div class="panel panel--right">
    <div class="copy" style="left:28px;top:22px;width:385px">
      <h2>Wrist Pain</h2>
      <p>Trigger finger occurs when the tendon that moves the finger gets pinched in its tunnel. This causes the finger to get stuck or stiff, which is often worse in the morning. This catching or locking can be quite painful. Grip may also cause pain. The finger may occasionally get stuck straight and be difficult to bend.</p>
      <p>Splinting may temporarily prevent the catching, but doesn't actually treat the problem. If caught early, a steroid injection can be curative. After 4-6 months the chance of an injection permanently curing the condition is lower, but still often worth a try.</p>
      <p>If the triggering returns following an injection, the problem can be definitively treated with a minimally-invasive Trigger Finger Release. This highly successful outpatient surgery is almost always a permanent cure. To see a video of a Trigger Finger Release please go to:</p>
      <p class="link">www.LimbForwardClinic.com</p>
      <h2>Trigger Finger</h2>
      <p>Wrist pain may have many causes and the diagnosis is best made by a fellowship-trained Hand Surgeon. The most common cause is DeQuervain's tendinitis, which causes pain on the thumb side of the wrist. This occurs when the tendons to the thumb and wrist get pinched in their tunnel. Pain is usually worse with lifting and gripping.</p>
      <p>DeQuervain's Tendinitis is common in mothers who repetitively lift children. It can also occur following frequent lifting with the thumb up, such as when pulling weeds, luggage or moving heavy objects.</p>
      <p>If the tendinitis recurs after injection, an outpatient tendon release is very effective. To prevent tendon subluxation after tunnel release, I lengthen the restraints that stabilize the tendon and repair them in a lengthened position. To see a video of a DeQuervain's Tendinitis Release please go to:</p>
      <p class="link">www.LimbForwardClinic.com</p>
    </div>
    <svg class="band" style="bottom:0" width="440" height="90" viewBox="0 0 440 90">
      <path d="M0 30C160 40 320 30 440 10V90H0Z" fill="var(--blue)"/>
      <path d="M0 22C160 32 320 22 440 2V12C320 32 160 42 0 32Z" fill="var(--teal)"/>
    </svg>
    <div class="ph" role="img" aria-label="Photo of a person holding a painful shoulder" style="left:130px;top:455px;width:90px;height:90px;border-radius:50%;border:4px solid var(--teal);background:linear-gradient(140deg,#8a7f78,#d49a86)"></div>
    <div class="ph" role="img" aria-label="Photo of a hand examining a sore elbow" style="left:240px;top:460px;width:85px;height:85px;border-radius:50%;border:4px solid var(--teal);background:linear-gradient(140deg,#f2ece8,#e0a896)"></div>
  </div>
  <div class="spine"></div>
</section>

</body>
</html>
```